New Web Design Project- Willowbrook Elders

Willowbrook Elders is the Capital regions premiere, non-medical, in-home care & companionship service that unites "junior-senior" caregivers with "senior-senior" care recipients so that senior-seniors can remain safe & independent in their own homes.
Our compassionate "junior-senior" caregivers are all retirees that have already enjoyed rewarding careers and/or have raised families of their own and feel the need to pay-it-forward with their care for older seniors.
Services include grocery shopping, medical or dental appointments, errands, meal preparation & cleanup, light housekeeping, bed making, laundry, hobbies, reading, transportation, entertainment, games, mobility assistance/transfers, respite care, light yard work, pet walking.

Target Market(s)

Grown children of senior-seniors between who are between 55-70, predominantly the daughters (female). End users of services (senior-seniors) are typically 80-100 years old and living in own homes

Industry/Entity Type

Medical

Coding

Coded - Design and coding required

Number of Pages Required

5+ page

Font styles to use
Sans Serif

Colors
3277b5
ec1f27

Requirements
Must have
• supporting photos on each page. Contact us page. Promotional video (done) attached that doesn't take viewers off my site (https://vidhost.example/q7Rk2mPzL4n).
• Also, need my downloadable brochure (attached).
• The following pages:
• Home. Services. About Us. News. Employment. Contact us. Junior-Seniors Assisting Senior-Seniors. Why non-medical in-home care. Who are junior-seniors?Financial effects of senior care. Do you need care? Does someone you love need care?
Should not have
• Any other photos or images other than what I've supplied.

```html
<!DOCTYPE html>
<html lang="en">
<head>
<meta charset="utf-8">
<title>Willowbrook Elders – Home</title>
<link href="https://fonts.googleapis.com/css2?family=Questrial&family=Raleway:wght@400;500;600&display=swap" rel="stylesheet">
<style>
:root{
  --navy:#0b4289;
  --red:#c21f2e;
  --ink:#2a2a2a;
  --muted:#6b6b6b;
  --panel:#f2f2f2;
  --footer:#2e2e2e;
  --footer-deep:#1f1f1f;
  --footer-text:#d0d0d0;
  --rule:#cfcfcf;
  --white:#ffffff;
}
*{box-sizing:border-box;margin:0;padding:0}
html,body{width:1200px;height:2965px;overflow:hidden}
body{position:relative;font-family:"Raleway",sans-serif;color:var(--ink);background:var(--white)}
.abs{position:absolute}
.heading{font-family:"Questrial",sans-serif;font-weight:400}

/* header */
.site-header{top:0;left:0;width:1200px;height:103px;background:var(--white)}
.brand{left:85px;top:16px;display:flex;align-items:center;gap:10px;white-space:nowrap}
.brand-mark{width:28px;height:28px;background:var(--navy);flex:none}
.brand-name{font-family:"Questrial",sans-serif;font-size:20px;color:var(--navy);line-height:1}
.brand-tag{left:85px;top:54px;font-size:10px;color:var(--navy);white-space:nowrap}
.top-item{top:20px;display:flex;align-items:center;gap:12px;font-size:13px;color:var(--ink);white-space:nowrap}
.top-item svg{fill:var(--navy);flex:none}
.appointment{left:905px;top:0;width:208px;height:55px;background:var(--navy);color:var(--white);display:flex;align-items:center;gap:12px;padding-left:20px;font-size:11.5px;font-weight:600;letter-spacing:.3px;white-space:nowrap}
.main-nav{top:68px;left:305px;width:808px;display:flex;justify-content:space-between;font-family:"Questrial",sans-serif;font-size:14px;letter-spacing:.4px}
.main-nav a{color:var(--ink);text-decoration:none}
.main-nav .sep{color:#c7c7c7}

.sub-nav{top:103px;left:0;width:1200px;height:43px;background:var(--red);display:flex;justify-content:center;gap:30px;align-items:center;font-size:11.5px;font-weight:600;color:var(--white);letter-spacing:.3px;white-space:nowrap}

.hero{top:146px;left:0;width:1200px;height:625px;background:linear-gradient(120deg,#6f4a38 0%,#b58d74 35%,#e7dcd3 60%,#c9b3a1 100%)}

/* services */
.arrow-btn{width:44px;height:44px;border:2px solid #b9b9b9;border-radius:50%;display:flex;align-items:center;justify-content:center}
.service-card{top:810px;width:326px;height:238px;background:var(--navy);color:var(--white);text-align:center;padding-top:30px}
.service-card h3{font-family:"Questrial",sans-serif;font-weight:400;font-size:16px;letter-spacing:1.5px;margin-top:14px}
.service-card p{font-size:11.5px;line-height:19px;margin:10px auto 0;width:270px}
.pill{display:inline-block;margin-top:16px;border:1px solid rgba(255,255,255,.7);border-radius:16px;padding:6px 22px;font-size:11px}

/* about */
.about-photo{top:1089px;left:0;width:510px;height:447px;background:linear-gradient(135deg,#7a8b5a,#c99bb0 55%,#e8d7de)}
.about-panel{top:1089px;left:510px;width:690px;height:447px;background:var(--panel)}
.about-title{top:1140px;left:560px;font-size:40px;color:var(--ink);white-space:nowrap}
.about-rule{top:1205px;left:560px;width:550px;height:1px;background:var(--rule)}
.about-rule::before{content:"";position:absolute;left:0;top:-2px;width:76px;height:4px;background:var(--red)}
.about-text{top:1253px;left:560px;width:550px;font-size:12.6px;line-height:24px;color:var(--muted)}
.btn-red{background:var(--red);color:var(--white);border-radius:26px;font-size:16px;display:flex;align-items:center;justify-content:center}
.about-btn{top:1436px;left:562px;width:172px;height:48px}

/* experts */
.section-title{left:0;width:1200px;text-align:center;font-size:42px}
.title-rule{left:395px;width:410px;height:1px;background:var(--rule)}
.title-rule::before{content:"";position:absolute;left:167px;top:-2px;width:76px;height:4px;background:var(--red)}
.expert{top:1750px;width:237px;text-align:center}
.expert-photo{height:170px}
.expert-name{margin-top:20px;font-family:"Questrial",sans-serif;font-size:23px}
.expert-role{margin-top:6px;font-size:11px;color:var(--muted);letter-spacing:.5px}
.expert-social{margin-top:14px;height:35px;background:var(--red);display:flex;gap:8px;justify-content:center;align-items:center}
.expert-social i{width:15px;height:15px;border-radius:50%;background:var(--white);display:block}

/* contact */
.contact-title{top:2155px;left:83px;font-size:33px}
.contact-item{left:85px;display:flex;gap:27px;align-items:flex-start}
.contact-icon{width:56px;height:56px;border-radius:50%;background:var(--red);display:flex;align-items:center;justify-content:center;flex:none}
.contact-item h4{font-family:"Questrial",sans-serif;font-weight:400;font-size:18px;margin-top:4px}
.contact-item p{font-size:15px;color:var(--muted);margin-top:8px}
.query{top:2125px;left:494px;width:706px;height:457px;background:var(--navy)}
.query-title{top:2158px;left:585px;font-size:32px;color:var(--white)}
.field{left:585px;width:522px;border:1px solid rgba(255,255,255,.8);color:var(--white);font-size:12px;padding:14px 24px}
.submit{top:2489px;left:585px;width:522px;height:48px;background:var(--red);color:var(--white);font-size:21px;display:flex;align-items:center;justify-content:center}

/* footer */
.site-footer{top:2582px;left:0;width:1200px;height:336px;background:var(--footer)}
.foot-brand{top:2650px;left:85px;display:flex;align-items:center;gap:10px}
.foot-brand .brand-name{color:var(--white);font-size:22px}
.foot-col-title{font-size:13px;color:var(--white)}
.foot-col-title::after{content:"";display:block;width:24px;height:2px;background:var(--red);margin-top:8px}
.foot-list{list-style:none;font-size:13px;line-height:31px;color:var(--footer-text)}
.foot-list li::before{content:"→";color:#8a8a8a;margin-right:16px;font-size:11px}
.foot-text{font-size:11px;line-height:18px;color:#bdbdbd}
.vline{width:1px;height:210px;background:#444}
.subscribe{top:2693px;left:880px;width:233px;height:40px;display:flex}
.subscribe span{flex:1;background:#d9d9d9;color:#666;font-size:10px;padding:13px 10px}
.subscribe b{width:42px;background:var(--red);display:flex;align-items:center;justify-content:center}
.legal{top:2918px;left:0;width:1200px;height:47px;background:var(--footer-deep);color:#bdbdbd;font-size:11px;display:flex;align-items:center;justify-content:center}
</style>
</head>
<body>

<header class="abs site-header">
  <div class="abs brand"><span class="brand-mark"></span><span class="brand-name">Willowbrook Elders</span></div>
  <div class="abs brand-tag">Junior Seniors assisting Senior Seniors</div>
  <span class="abs top-item" style="left:322px"><svg width="15" height="15" viewBox="0 0 24 24"><path d="M6.6 10.8a15 15 0 0 0 6.6 6.6l2.2-2.2c.3-.3.7-.4 1-.2 1.1.4 2.3.6 3.6.6.6 0 1 .4 1 1V20c0 .6-.4 1-1 1A17 17 0 0 1 3 4c0-.6.4-1 1-1h3.5c.6 0 1 .4 1 1 0 1.3.2 2.5.6 3.6.1.3 0 .7-.2 1z"/></svg>(555) 310-4472</span>
  <span class="abs top-item" style="left:462px"><svg width="17" height="13" viewBox="0 0 24 18"><path d="M0 0h24v18H0z"/><path d="M1 1l11 9 11-9" fill="none" stroke="#fff" stroke-width="2"/></svg>hello@willowbrookelders.example</span>
  <span class="abs top-item" style="left:716px"><svg width="15" height="15" viewBox="0 0 24 24"><circle cx="12" cy="12" r="11"/><path d="M12 6v6l4 3" fill="none" stroke="#fff" stroke-width="2"/></svg>Mon-Sat: 07:00 - 17:00</span>
  <div class="abs appointment"><svg width="20" height="20" viewBox="0 0 24 24" fill="none" stroke="#fff" stroke-width="2"><rect x="3" y="5" width="18" height="16"/><path d="M3 10h18M8 2v5M16 2v5"/></svg>MAKE AN APPOINTMENT</div>
  <nav class="abs main-nav">
    <a>HOME</a><span class="sep">|</span><a>SERVICES</a><span class="sep">|</span><a>ABOUT US</a><span class="sep">|</span><a>NEWS</a><span class="sep">|</span><a>EMPLOYMENT</a><span class="sep">|</span><a>CONTACT US</a>
  </nav>
</header>

<nav class="abs sub-nav">
  <span>JUNIOR-SENIORS ASSISTING SENIOR-SENIORS</span><span>WHY NON-MEDICAL IN-HOME CARE</span><span>WHO ARE JUNIOR -SENIORS?</span><span>FINANCIAL EFFECTS OF SENIOR CARE</span><span>DO YOU NEED CARE?</span>
</nav>

<div class="abs hero" role="img" aria-label="Photo: an older woman and a caregiver preparing a salad together in a kitchen"></div>

<section>
  <div class="abs arrow-btn" style="top:893px;left:21px"><svg width="18" height="14" viewBox="0 0 18 14" fill="none" stroke="#b9b9b9" stroke-width="2"><path d="M17 7H2M7 1L1 7l6 6"/></svg></div>
  <div class="abs arrow-btn" style="top:893px;left:1135px"><svg width="18" height="14" viewBox="0 0 18 14" fill="none" stroke="#b9b9b9" stroke-width="2"><path d="M1 7h15M11 1l6 6-6 6"/></svg></div>

  <article class="abs service-card" style="left:85px">
    <svg width="44" height="40" viewBox="0 0 44 40" fill="#fff"><path d="M22 20c-4-3-8-6-8-10a4 4 0 0 1 8-1 4 4 0 0 1 8 1c0 4-4 7-8 10z"/><path d="M4 22l8 10h10v-4h-8l-6-8zM40 22l-8 10H22v-4h8l6-8z"/></svg>
    <h3>COMPANIONSHIP</h3>
    <p>A companion-Junior Senior is like the friend who drops by to see how you are fairing</p>
    <span class="pill">Learn More</span>
  </article>
  <article class="abs service-card" style="left:435px">
    <svg width="40" height="40" viewBox="0 0 40 40" fill="#fff"><path d="M20 3a14 14 0 0 0-14 14c0 5 2 8 5 10v10h14v-5h5a3 3 0 0 0 3-3v-5h4l-4-7A14 14 0 0 0 20 3z"/></svg>
    <h3>ALZHEIMERS CARE</h3>
    <p>The Regional Memory Care Council of the Valley provides ongoing training for our Junior Seniors</p>
    <span class="pill">Learn More</span>
  </article>
  <article class="abs service-card" style="left:785px">
    <svg width="50" height="40" viewBox="0 0 50 40" fill="#fff"><path d="M2 10h28v18H2zM30 16h10l7 7v5H30z"/><circle cx="11" cy="31" r="4"/><circle cx="39" cy="31" r="4"/></svg>
    <h3>GENERAL TRANSPORTATION</h3>
    <p>A companion-Junior Senior is like the friend who drops by to see how you are fairing</p>
    <span class="pill">Learn More</span>
  </article>
</section>

<section>
  <div class="abs about-photo" role="img" aria-label="Photo: two older women laughing together on a porch sofa"></div>
  <div class="abs about-panel"></div>
  <h2 class="abs heading about-title">About Willowbrook Elders</h2>
  <div class="abs about-rule"></div>
  <p class="abs about-text">Willowbrook EldersTM is a wholly owned New York State LLC, not a franchise, and was founded in 2012 by covered by a $2 million general liability insurance policy, as well as workers compensation (NYS disability insurance). In order to become Junior Seniors, our caregivers go through extensive local, state and federal background checks, as well as personal interviews. We follow through on all personal and professional references and ensure that applicants are first-aid and CPR certified.</p>
  <div class="abs btn-red about-btn">Learn More</div>
</section>

<section>
  <h2 class="abs heading section-title" style="top:1605px">Some of our Experts</h2>
  <div class="abs title-rule" style="top:1682px"></div>
  <div class="abs arrow-btn" style="top:1862px;left:24px;width:40px;height:40px;border-width:1px"><svg width="8" height="12" viewBox="0 0 8 12" fill="none" stroke="#999" stroke-width="1.5"><path d="M7 1L2 6l5 5"/></svg></div>
  <div class="abs arrow-btn" style="top:1862px;left:1136px;width:40px;height:40px;border-width:1px"><svg width="8" height="12" viewBox="0 0 8 12" fill="none" stroke="#999" stroke-width="1.5"><path d="M1 1l5 5-5 5"/></svg></div>

  <article class="abs expert" style="left:85px">
    <div class="expert-photo" role="img" aria-label="Photo: a smiling caregiver standing in a bright room" style="background:linear-gradient(135deg,#d9e6ee,#6f8f92 60%,#2f5c6c)"></div>
    <div class="expert-name">Nora Ellis</div><div class="expert-role">WORKER</div>
    <div class="expert-social"><i></i><i></i><i></i></div>
  </article>
  <article class="abs expert" style="left:350px">
    <div class="expert-photo" role="img" aria-label="Photo: a caregiver working on a laptop" style="background:linear-gradient(135deg,#f2f0ec,#c9b8a6 55%,#6f86a8)"></div>
    <div class="expert-name">Maribel</div><div class="expert-role">WORKER</div>
    <div class="expert-social"><i></i><i></i><i></i></div>
  </article>
  <article class="abs expert" style="left:613px">
    <div class="expert-photo" role="img" aria-label="Photo: a caregiver helping an older woman at home" style="background:linear-gradient(135deg,#4a3a30,#a58a72 55%,#d8cfc5)"></div>
    <div class="expert-name">Claire Donovan</div><div class="expert-role">WORKER</div>
    <div class="expert-social"><i></i><i></i><i></i></div>
  </article>
  <article class="abs expert" style="left:876px">
    <div class="expert-photo" role="img" aria-label="Photo: a caregiver and an older man looking at a tablet" style="background:linear-gradient(135deg,#5c5450,#a58f80 55%,#e3dad3)"></div>
    <div class="expert-name">Ruth Adler</div><div class="expert-role">WORKER</div>
    <div class="expert-social"><i></i><i></i><i></i></div>
  </article>
</section>

<section>
  <h2 class="abs heading contact-title">Contact Us</h2>
  <div class="abs contact-item" style="top:2230px">
    <span class="contact-icon"><svg width="18" height="22" viewBox="0 0 18 22" fill="#fff"><path d="M9 0a8 8 0 0 0-8 8c0 6 8 14 8 14s8-8 8-14a8 8 0 0 0-8-8z"/><circle cx="9" cy="8" r="3" fill="#c21f2e"/></svg></span>
    <div><h4>Address</h4><p>Elder Circle Partners, LLC dba</p></div>
  </div>
  <div class="abs contact-item" style="top:2313px">
    <span class="contact-icon"><svg width="20" height="20" viewBox="0 0 24 24" fill="#fff"><path d="M6.6 10.8a15 15 0 0 0 6.6 6.6l2.2-2.2c.3-.3.7-.4 1-.2 1.1.4 2.3.6 3.6.6.6 0 1 .4 1 1V20c0 .6-.4 1-1 1A17 17 0 0 1 3 4c0-.6.4-1 1-1h3.5c.6 0 1 .4 1 1 0 1.3.2 2.5.6 3.6.1.3 0 .7-.2 1z"/></svg></span>
    <div><h4>Phone</h4><p>(555) 310-4472</p></div>
  </div>
  <div class="abs contact-item" style="top:2396px">
    <span class="contact-icon"><svg width="20" height="15" viewBox="0 0 24 18"><path d="M0 0h24v18H0z" fill="#fff"/><path d="M1 1l11 9 11-9" fill="none" stroke="#c21f2e" stroke-width="2"/></svg></span>
    <div><h4>Email</h4><p>hello@willowbrookelders.example</p></div>
  </div>
  <div class="abs contact-item" style="top:2477px">
    <span class="contact-icon"><svg width="20" height="20" viewBox="0 0 24 24"><circle cx="12" cy="12" r="11" fill="#fff"/><path d="M12 6v6l4 3" fill="none" stroke="#c21f2e" stroke-width="2"/></svg></span>
    <div><h4>Opening Hours</h4><p>Mon-Fri: 8:00 AM – 9:00 PM</p></div>
  </div>

  <div class="abs query"></div>
  <h2 class="abs heading query-title">Make A Query</h2>
  <div class="abs field" style="top:2238px;height:49px">Name...</div>
  <div class="abs field" style="top:2301px;height:50px">Phone...</div>
  <div class="abs field" style="top:2365px;height:108px">Message...</div>
  <div class="abs submit">Submit</div>
</section>

<footer class="abs site-footer"></footer>
<div class="abs foot-brand"><span class="brand-mark" style="background:var(--red)"></span><span class="brand-name">Willowbrook Elders</span></div>
<div class="abs foot-col-title" style="top:2779px;left:85px">About Us</div>
<p class="abs foot-text" style="top:2808px;left:85px;width:230px">Totam rem aperiam, eaque ipsa quae ab illo inventore veritatis et quasi architecto beatae vitae dicta sunt explicabo.</p>

<div class="abs vline" style="top:2640px;left:355px"></div>
<div class="abs foot-col-title" style="top:2648px;left:423px">Quick Links</div>
<ul class="abs foot-list" style="top:2683px;left:413px">
  <li>Home</li><li>Services</li><li>About Us</li><li>News</li><li>Employment</li><li>Contact us</li>
</ul>
<div class="abs vline" style="top:2640px;left:578px"></div>
<div class="abs foot-col-title" style="top:2648px;left:641px">Services</div>
<ul class="abs foot-list" style="top:2683px;left:641px">
  <li>Meal preparation</li><li>Light housekeeping</li><li>Bed Making</li><li>Light yard work</li><li>Pet walking</li><li>Laundry</li>
</ul>
<div class="abs vline" style="top:2640px;left:840px"></div>
<div class="abs foot-col-title" style="top:2654px;left:880px">Subscribe Newsletter</div>
<div class="abs subscribe"><span>Enter Your Email ID...</span><b><svg width="16" height="12" viewBox="0 0 24 18"><path d="M0 0h24v18H0z" fill="#fff"/><path d="M1 1l11 9 11-9" fill="none" stroke="#c21f2e" stroke-width="2"/></svg></b></div>
<p class="abs foot-text" style="top:2752px;left:880px;width:233px">Totam rem aperiam, eaque ipsa quae ab illo inventore veritatis et quasi architecto</p>

<div class="abs legal">willowbrookelders.example 2017. All rights reserved</div>

</body>
</html>
```